Bramblecrest Wellness Web Page

To create a web page that has the number 1 goal of converting Google Ad / Facebook Ads clicks into paying customers.
The site will feed into a web application where travellers can enter their trip and purchase a Roamwell Kit Guide.
The page / site needs to be able to tell people what we do and encourage them to start the process of getting a Roamwell Kit Guide.
It should be a wordpress theme.
Please see the attached brief for more information.

```html
<!DOCTYPE html>
<html lang="en">
<head>
<meta charset="utf-8">
<title>Bramblecrest Wellness — Roamwell Kit Guide</title>
<link rel="stylesheet" href="https://fonts.googleapis.com/css2?family=Poppins:wght@400;500;600;700&display=swap">
<style>
:root{
  --navy:#1c2b57;
  --sky:#4aa8d8;
  --ocean:#1a6a95;
  --slate:#5f6b70;
  --mist:#eeeeee;
  --band:#f6f7f8;
  --text:#2a2f3a;
  --white:#ffffff;
}
*{box-sizing:border-box;margin:0;padding:0}
html,body{width:1200px;height:3715px;overflow:hidden}
body{position:relative;background:var(--white);font-family:"Poppins",Arial,sans-serif;color:var(--text)}
.abs{position:absolute}
.btn{position:absolute;display:flex;align-items:center;justify-content:center;border:2px solid var(--ocean);border-radius:10px;color:var(--ocean);font-weight:600;font-size:13px;background:var(--white)}
.btn--solid{font-weight:700;color:var(--navy);border-color:var(--ocean);background:transparent;font-size:14px}
.heading{font-weight:700;color:var(--navy);line-height:1.1}
.heading .accent{color:var(--sky)}
.para{font-family:Arial,sans-serif;font-size:11px;line-height:2;color:var(--text)}
/* hero */
.hero{position:absolute;left:0;top:0;width:1200px;height:573px;background:linear-gradient(180deg,#cfe3ee 0%,#bdd6e2 55%,#a9b9a6 100%)}
.brand{position:absolute;display:flex;align-items:center;gap:8px;font-weight:600;color:var(--ocean);font-size:16px}
.brand .dot{width:14px;height:14px;border-radius:50%;background:var(--sky)}
.nav{position:absolute;top:45px;font-size:12px;color:var(--ocean)}
.hero-title{left:224px;top:205px;font-size:50px;font-weight:700;color:var(--navy);line-height:0.95}
.hero-sub{left:224px;top:311px;font-size:15px;color:var(--navy)}
.select{position:absolute;top:368px;height:36px;background:rgba(255,255,255,0.85);border-radius:5px;display:flex;align-items:center;justify-content:space-between;padding:0 12px;font-size:11px;color:#8a93a0}
.select .caret{color:var(--navy);font-size:9px}
.hero-visual{left:650px;top:130px;width:360px;height:443px;background:linear-gradient(180deg,rgba(190,215,228,0) 0%,#a7c9dc 30%,#c9ab92 70%,#b59a80 100%)}
/* about */
.map{left:0;top:635px;width:606px;height:390px;background:linear-gradient(120deg,#b9a488 0%,#d8bea3 40%,#9aaab9 75%,#5e7188 100%);opacity:0.85}
.feature-num{font-size:15px;font-weight:600;color:var(--navy)}
.feature-title{font-size:14px;font-weight:600;color:var(--sky);line-height:1.15;margin-top:14px}
.feature-text{font-family:Arial,sans-serif;font-size:10px;line-height:1.4;color:var(--text);margin-top:16px}
.feature{position:absolute;width:150px}
.readmore-card{left:811px;top:1327px;width:163px;height:166px;border-radius:6px;background:linear-gradient(160deg,#dde7ea 0%,#b9c6cc 55%,#6e6862 100%);display:flex;align-items:center;justify-content:center;font-weight:600;font-size:14px;color:var(--navy)}
/* destinations */
.card{position:absolute;top:1680px;width:239px;height:245px;background:var(--white);border-radius:6px;box-shadow:0 2px 10px rgba(0,0,0,0.08);overflow:hidden}
.card .photo{height:195px}
.card .name{position:absolute;left:19px;top:203px;font-size:15px;color:var(--navy)}
.card .season{position:absolute;left:19px;top:225px;font-size:9px;color:var(--sky)}
.card .btn{left:149px;top:207px;width:80px;height:30px;font-size:11px;font-weight:500;border-width:1.5px}
/* contents */
.item{position:absolute;width:170px;text-align:center}
.item .title{font-size:13px;font-weight:600;color:var(--ocean);line-height:1.15}
.item .text{font-family:Arial,sans-serif;font-size:9.5px;line-height:1.45;color:#4a5060;margin-top:10px}
.item svg{display:block;margin:0 auto 8px}
/* articles */
.article-photo{position:absolute;top:3108px;width:351px;height:115px;border-radius:4px}
.article-title{position:absolute;top:3250px;font-size:28px;font-weight:700;color:var(--navy);line-height:1.05}
.article-title .accent{color:var(--sky)}
.swatch{position:absolute;left:68px;width:23px;height:23px;border-radius:50%}
/* footer */
.footer{position:absolute;left:0;top:3562px;width:1200px;height:153px;background:#f1f2f3}
.flink{position:absolute;font-family:Arial,sans-serif;font-size:10.5px;color:var(--text);line-height:2.1}
.social{position:absolute;top:3669px;width:13px;height:13px;border-radius:50%;background:var(--navy)}
</style>
</head>
<body>

<!-- HERO -->
<header class="hero" role="img" aria-label="Soft blue mountain landscape photograph behind the header"></header>
<div class="brand" style="left:224px;top:42px;color:var(--navy)"><span class="dot"></span>Bramblecrest Wellness</div>
<span class="nav" style="left:637px">About Us</span>
<span class="nav" style="left:711px">Conatact</span>
<span class="nav" style="left:789px">What we Do</span>
<div class="btn btn--solid" style="left:870px;top:35px;width:105px;height:36px">BUY NOW</div>

<h1 class="abs hero-title">Roamwell<br>Kit Guide</h1>
<p class="abs hero-sub">Your Guide to Safe and Healthy Journeys</p>
<div class="select" style="left:225px;width:208px"><span>
<svg width="9" height="11" viewBox="0 0 9 11" style="vertical-align:-1px"><path d="M4.5 0a4 4 0 0 1 4 4c0 3-4 7-4 7s-4-4-4-7a4 4 0 0 1 4-4z" fill="#4aa8d8"/></svg> Trip To</span><span class="caret">▼</span></div>
<div class="select" style="left:443px;width:143px"><span><span style="color:var(--sky)">✳</span> Season</span><span class="caret">▼</span></div>
<div class="btn btn--solid" style="left:226px;top:421px;width:100px;height:38px">BUY NOW</div>

<div class="abs hero-visual" role="img" aria-label="Hand holding a small globe framed by a blue shield outline"></div>

<!-- ABOUT -->
<div class="abs map" role="img" aria-label="World map filled with travel photography and location pins"></div>
<h2 class="abs heading" style="left:629px;top:695px;font-size:37px">What is<br><span class="accent">Bramblecrest Wellness?</span></h2>
<p class="abs para" style="left:629px;top:808px;width:395px">At Bramblecrest Wellness, we understand the importance of staying healthy and safe while exploring the world. We specialize in providing comprehensive and personalized roamwell kit guides, designed to equip you with essential information and recommendations specific to your travel destination.</p>
<div class="btn" style="left:633px;top:922px;width:103px;height:34px;font-size:11px;border-width:1.5px">Read more</div>

<!-- WHY BUY -->
<h2 class="abs heading" style="left:225px;top:1118px;font-size:35px">Why buy a<br><span class="accent">roamwell kit guide</span></h2>
<p class="abs para" style="left:225px;top:1210px;width:330px">At Bramblecrest Wellness, we understand the importance of staying healthy and safe while exploring the world.</p>

<div class="feature" style="left:623px;top:1128px"><div class="feature-num">01</div><div class="feature-title">Customized<br>Destination Insights</div><div class="feature-text">Our roamwell kit guides are tailored to your unique travel plans.</div></div>
<div class="feature" style="left:828px;top:1128px"><div class="feature-num">02</div><div class="feature-title">Expert<br>Recommendations</div><div class="feature-text">Our team of experienced travel health professionals carefully analyzes the health risks associated with your destination</div></div>
<div class="feature" style="left:225px;top:1334px"><div class="feature-num">03</div><div class="feature-title">Convenience<br>and Accessibility</div><div class="feature-text">Roamwell Kit Guide offers an online platform that allows you to easily access your personalized travel health guide.</div></div>
<div class="feature" style="left:418px;top:1334px"><div class="feature-num">04</div><div class="feature-title">Timely<br>Updates and Alerts</div><div class="feature-text">We continuously monitor global health updates and alerts to keep our travel health guides current and relevant.</div></div>
<div class="feature" style="left:626px;top:1334px"><div class="feature-num">05</div><div class="feature-title">Peace of Mind</div><div class="feature-text">With our roamwell kit guides, you can embark on your journey with confidence.</div></div>
<div class="abs readmore-card" role="img" aria-label="Passports on a table in front of a blurred city view">Read more</div>

<!-- DESTINATIONS -->
<svg class="abs" style="left:227px;top:1632px" width="18" height="24" viewBox="0 0 18 24" aria-hidden="true"><circle cx="9" cy="9" r="8" fill="#1a6a95"/><circle cx="9" cy="9" r="3" fill="#fff"/><path d="M5 16 L9 23 L13 16Z" fill="#1a6a95"/></svg>
<div class="abs" style="left:260px;top:1633px;font-size:16px;font-weight:600;color:var(--navy)">Popular <span style="color:var(--sky)">Bramblecrest Picks</span></div>

<svg class="abs" style="left:173px;top:1794px" width="24" height="18" viewBox="0 0 24 18" aria-hidden="true"><path d="M22 9H3M10 2L3 9l7 7" fill="none" stroke="#b7bcc4" stroke-width="2.4" stroke-linecap="round"/></svg>
<svg class="abs" style="left:1000px;top:1794px" width="24" height="18" viewBox="0 0 24 18" aria-hidden="true"><path d="M2 9h19M14 2l7 7-7 7" fill="none" stroke="#1a6a95" stroke-width="2.4" stroke-linecap="round"/></svg>

<div class="card" style="left:225px"><div class="photo" role="img" aria-label="Tiered temple pagoda by a lake under a cloudy sky" style="background:linear-gradient(180deg,#9aa7b4 0%,#c7ccd0 45%,#4d5a44 80%,#2e3a2a 100%)"></div><div class="name">Bali</div><div class="season">✳ Summer</div><div class="btn">Buy Brief</div></div>
<div class="card" style="left:480px"><div class="photo" role="img" aria-label="Whitewashed hillside village above a deep blue sea" style="background:linear-gradient(180deg,#3f8fd4 0%,#9cc8ee 40%,#e9eef2 65%,#6d6a6a 100%)"></div><div class="name">Greece</div><div class="season">✳ Summer</div><div class="btn">Buy Brief</div></div>
<div class="card" style="left:736px"><div class="photo" role="img" aria-label="Canal lined with colourful old buildings" style="background:linear-gradient(180deg,#d9c3b1 0%,#c0927b 45%,#4fa6a6 75%,#2d7f86 100%)"></div><div class="name">Italy</div><div class="season">✳ Summer</div><div class="btn">Buy Brief</div></div>

<!-- CONTENTS -->
<h2 class="abs heading" style="left:0;top:2033px;width:1200px;text-align:center;font-size:35px">What is in a<br><span class="accent">roamwell kit guide</span></h2>
<p class="abs para" style="left:0;top:2126px;width:1200px;text-align:center">At Bramblecrest Wellness, we understand the importance of staying healthy and safe while exploring the world.</p>

<svg class="abs" style="left:0;top:2150px" width="1200" height="870" viewBox="0 0 1200 870" aria-hidden="true">
  <path d="M0 50 C150 0 450 0 600 50 C750 0 1050 0 1200 50 L1200 820 C1050 870 750 870 600 820 C450 870 150 870 0 820Z" fill="#f6f7f8"/>
  <circle cx="600" cy="406" r="275" fill="none" stroke="#dfe3e7" stroke-width="1.2" stroke-dasharray="4 5"/>
</svg>
<div class="abs" role="img" aria-label="Traveller looking out over a rocky blue coastline, overlaid with a checklist icon" style="left:467px;top:2423px;width:266px;height:266px;border-radius:50%;background:radial-gradient(circle at 45% 40%,#4d8fc0 0%,#1f5f92 55%,#123f66 100%)"></div>
<svg class="abs" style="left:545px;top:2505px" width="110" height="100" viewBox="0 0 110 100" aria-hidden="true" fill="none" stroke="#ffffff" stroke-width="3">
  <rect x="20" y="6" width="54" height="76" rx="3"/><rect x="48" y="14" width="48" height="70" rx="3"/>
  <path d="M28 20h30M28 30h26M56 30l4 4 6-8M56 46l4 4 6-8M56 62l4 4 6-8M74 34h14M74 50h14M74 66h14"/>
  <circle cx="34" cy="56" r="11"/><path d="M26 64L12 80"/>
</svg>

<div class="item" style="left:515px;top:2262px">
  <svg width="46" height="46" viewBox="0 0 46 46" fill="none" stroke="#4aa8d8" stroke-width="2"><path d="M23 40S5 28 5 15a9 9 0 0 1 18-2 9 9 0 0 1 18 2c0 13-18 25-18 25z"/><path d="M8 22h8l3-6 4 10 3-6h12"/><path d="M29 26l7 13h-14z" fill="#fff"/><path d="M29 30v4M29 36v1"/></svg>
  <div class="title">Health Risks</div><div class="text">It outlines the prevalent health risks and potential hazards associated with the destination</div></div>
<div class="item" style="left:267px;top:2364px">
  <svg width="50" height="50" viewBox="0 0 50 50" fill="none" stroke="#4aa8d8" stroke-width="2"><path d="M12 8l30 30M16 12l-6 6M38 34l-4 4M28 18l-14 14M40 40l6 6"/><rect x="8" y="30" width="10" height="16" rx="2"/><rect x="20" y="34" width="10" height="12" rx="2"/></svg>
  <div class="title">Vaccinations and<br>Immunizations</div><div class="text">The brief lists the recommended and required vaccinations for the destination.</div></div>
<div class="item" style="left:767px;top:2364px">
  <svg width="44" height="50" viewBox="0 0 44 50" fill="none" stroke="#4aa8d8" stroke-width="2"><rect x="8" y="4" width="20" height="7" rx="1"/><rect x="6" y="11" width="24" height="34" rx="3"/><path d="M18 22v10M13 27h10"/><rect x="24" y="32" width="16" height="10" rx="5" transform="rotate(-30 32 37)"/></svg>
  <div class="title">Medications and<br>Prophylaxis</div><div class="text">It provides information on any specific medications or prophylactic treatments recommended...</div></div>
<div class="item" style="left:267px;top:2582px">
  <svg width="58" height="34" viewBox="0 0 58 34" fill="none" stroke="#4aa8d8" stroke-width="2"><path d="M12 8c10-6 24-6 34 0v16c-10 8-24 8-34 0z"/><path d="M12 12H5v8h7M46 12h7v8h-7M18 14h22M18 20h22"/></svg>
  <div class="title">Health and Safety<br>Precautions</div><div class="text">The brief offers practical advice on staying safe and healthy during the trip.</div></div>
<div class="item" style="left:767px;top:2566px">
  <svg width="50" height="50" viewBox="0 0 50 50" fill="none" stroke="#4aa8d8" stroke-width="2"><path d="M10 16c-4 4 2 16 10 24s20 14 24 10l-6-8-6 3c-4-2-9-7-11-11l3-6z"/><rect x="26" y="10" width="16" height="14" rx="2"/><path d="M34 13v8M30 17h8M28 4l2 3M40 4l-2 3M34 2v3"/></svg>
  <div class="title">Emergency Contacts<br>and Medical Facilities</div><div class="text">It provides important contact information for local emergency services, medical facilities...</div></div>
<div class="item" style="left:515px;top:2722px">
  <svg width="46" height="46" viewBox="0 0 46 46" fill="none" stroke="#4aa8d8" stroke-width="2"><path d="M23 4l12 5v9c0 8-6 13-12 15-6-2-12-7-12-15V9z"/><path d="M18 18l4 4 7-8"/><path d="M4 26l6 14h8M42 26l-6 14h-8"/></svg>
  <div class="title">Travel Insurance</div><div class="text">The brief may emphasize the importance of travel insurance, including medical coverage.</div></div>

<div class="btn btn--solid" style="left:551px;top:2902px;width:100px;height:38px;border-radius:19px">BUY NOW</div>

<!-- ARTICLES -->
<div class="swatch" style="top:3122px;background:var(--navy)"></div>
<div class="swatch" style="top:3151px;background:var(--ocean)"></div>
<div class="swatch" style="top:3179px;background:var(--sky)"></div>
<div class="swatch" style="top:3207px;background:var(--slate)"></div>
<div class="swatch" style="top:3235px;background:var(--mist)"></div>

<div class="article-photo" style="left:225px;background:linear-gradient(90deg,#8d8f93 0%,#d9d9dc 40%,#f3f3f5 70%,#9fa3aa 100%)" role="img" aria-label="Blurred doctor holding a vaccine syringe"></div>
<div class="article-photo" style="left:624px;background:linear-gradient(120deg,#c9a88c 0%,#e2c6ad 50%,#b58e70 100%)" role="img" aria-label="Close view of a mosquito on skin"></div>

<h3 class="article-title" style="left:225px">What vaccines <span class="accent">do I<br>need for...</span></h3>
<h3 class="article-title" style="left:627px">What antimalarials<br><span class="accent">do I need for...</span></h3>
<p class="abs para" style="left:225px;top:3322px;width:345px;line-height:1.6">At Bramblecrest Wellness, we understand the importance of staying healthy and safe while exploring the world.</p>
<p class="abs para" style="left:627px;top:3322px;width:320px;line-height:1.6">At Bramblecrest Wellness, we understand the importance of staying healthy and safe while exploring the world.</p>
<div class="btn" style="left:226px;top:3376px;width:120px;height:35px;font-size:11px;border-width:1.5px">Let's Get know</div>
<div class="btn" style="left:628px;top:3376px;width:120px;height:35px;font-size:11px;border-width:1.5px">Let's Get know</div>

<!-- FOOTER -->
<footer class="footer"></footer>
<div class="brand" style="left:229px;top:3590px;font-size:14px;color:var(--navy)"><span class="dot"></span>Bramblecrest Wellness</div>
<div class="flink" style="left:481px;top:3584px">About<br>Contact<br>Why Us</div>
<div class="flink" style="left:602px;top:3584px">Accessibility<br>terms<br>Help</div>
<div class="abs" style="left:746px;top:3585px;font-size:12px;font-weight:600;color:var(--sky)">Have questions ? We have answers.</div>
<div class="flink" style="left:756px;top:3605px">
  <svg width="11" height="11" viewBox="0 0 11 11" style="vertical-align:-1px" fill="none" stroke="#1c2b57"><path d="M2 1l2 2-1 2c1 1 2 2 3 3l2-1 2 2-2 1C4 10 1 7 1 3z"/></svg>&nbsp; 1-800-555-0142 (800-555-0143)<br>
  <svg width="11" height="9" viewBox="0 0 11 9" style="vertical-align:-1px" fill="none" stroke="#1c2b57"><rect x="0.5" y="0.5" width="10" height="8"/><path d="M0.5 0.5l5 4 5-4"/></svg>&nbsp; hello@bramblecrestwellness.example</div>
<div class="social" style="left:754px"></div>
<div class="social" style="left:775px"></div>
<div class="social" style="left:796px"></div>
<div class="social" style="left:817px"></div>
<div class="abs" style="left:231px;top:3674px;font-family:Arial,sans-serif;font-size:8.5px;color:#8a8f98">© copyright 2023 bramblecrestwellness. All right reserved</div>

</body>
</html>
```